Social Media Graphics - Harbor Climb REVISED

Create 6-7 individual social media graphics (square size) to encourage folks to join our online course called:

The Lantern Ledger Plan
How to Launch a Multi-Million Business From Scratch
Sign Up Today!

IMPORTANT: Make the largest and most prominent text on the graphic be: How to Launch a Multi-Million Business From Scratch

For the color scheme of the graphics, let's try a blue color palette; make sure the graphics appeal to both men and women

Make sure each graphic contains 1 of the 3 pics attached (crop pic as needed); and make sure one of the graphics is all TEXT only.

Target Market(s)

men and women looking to start a business

Industry/Entity Type

Entrepreneurship

Colors
0054AA
0677BA
7BADD7
CADEEF
E8F1F8

Requirements
Must have
• All the text and use the 3 pics provided; one graphic can be all text; Simple, modern design that's easy to read

```html
<!DOCTYPE html>
<html lang="en">
<head>
<meta charset="utf-8">
<title>The Lantern Ledger Plan – Social Graphic</title>
<link rel="stylesheet" href="https://fonts.googleapis.com/css2?family=Bebas+Neue&family=Poppins:wght@500;700;800&display=swap">
<style>
  :root {
    --stage: #5e5e5e;
    --navy-deep: #021232;
    --navy: #0a2d63;
    --navy-mid: #0f3f80;
    --ink: #0b1f45;
    --white: #ffffff;
    --teal: #0677ba;
    --cyan: #18c4f7;
    --butter: #f6ef8c;
    --gold: #c99a2c;
    --gold-light: #f3e57d;
    --grid: rgba(123, 173, 215, 0.18);
    --photo-a: #2e4f7d;
    --photo-b: #1a2336;
  }
  html, body {
    margin: 0;
    width: 1195px;
    height: 1200px;
    overflow: hidden;
    background: var(--stage);
  }
  .post {
    position: absolute;
    left: 104px;
    top: 105px;
    width: 988px;
    height: 989px;
    display: block;
  }
  .title-word { font-family: "Bebas Neue", "Oswald", sans-serif; fill: var(--white); font-size: 91px; }
  .title-highlight { fill: var(--teal); }
  .title-box { fill: var(--white); }
  .kicker { font-family: "Poppins", sans-serif; font-weight: 500; fill: var(--butter); }
  .headline-main { font-family: "Poppins", sans-serif; font-weight: 800; font-size: 194px; fill: url(#goldText); }
  .headline-sub { font-family: "Bebas Neue", "Oswald", sans-serif; fill: var(--cyan); font-size: 93px; }
  .headline-end { font-family: "Bebas Neue", "Oswald", sans-serif; fill: var(--cyan); font-size: 154px; }
  .headline-end .accent { fill: var(--white); }
  .cta-box { fill: var(--white); }
  .cta-label { font-family: "Poppins", sans-serif; font-weight: 800; font-size: 24px; fill: var(--ink); }
  .chart-bar { fill: none; stroke: var(--grid); stroke-width: 2; }
  .chart-line { fill: none; stroke: rgba(123, 173, 215, 0.35); stroke-width: 3; }
  .chart-dot { fill: none; stroke: rgba(123, 173, 215, 0.35); stroke-width: 2; }
</style>
</head>
<body>
<svg class="post" viewBox="0 0 988 989" xmlns="http://www.w3.org/2000/svg" aria-labelledby="postTitle">
  <title id="postTitle">The Lantern Ledger Plan – How to Launch a Multi-Million Business From Scratch</title>
  <defs>
    <linearGradient id="bgFill" x1="0" y1="0" x2="0" y2="1">
      <stop offset="0" stop-color="var(--navy-deep)"/>
      <stop offset="0.55" stop-color="var(--navy)"/>
      <stop offset="1" stop-color="var(--navy-mid)"/>
    </linearGradient>
    <linearGradient id="goldText" x1="0" y1="0" x2="1" y2="0">
      <stop offset="0" stop-color="var(--gold)"/>
      <stop offset="0.45" stop-color="var(--gold-light)"/>
      <stop offset="1" stop-color="var(--butter)"/>
    </linearGradient>
    <linearGradient id="beamFill" x1="0" y1="0" x2="0" y2="1">
      <stop offset="0" stop-color="var(--gold)"/>
      <stop offset="0.5" stop-color="var(--gold-light)"/>
      <stop offset="1" stop-color="var(--butter)"/>
    </linearGradient>
    <linearGradient id="photoFill" x1="0" y1="0" x2="0" y2="1">
      <stop offset="0" stop-color="var(--photo-a)"/>
      <stop offset="1" stop-color="var(--photo-b)"/>
    </linearGradient>
  </defs>

  <rect class="background" width="988" height="989" fill="url(#bgFill)"/>

  <g class="growth-chart">
    <rect class="chart-bar" x="70" y="480" width="30" height="280"/>
    <rect class="chart-bar" x="220" y="470" width="30" height="290"/>
    <rect class="chart-bar" x="340" y="500" width="30" height="260"/>
    <rect class="chart-bar" x="610" y="460" width="30" height="300"/>
    <rect class="chart-bar" x="740" y="420" width="30" height="340"/>
    <rect class="chart-bar" x="880" y="440" width="30" height="320"/>
    <polyline class="chart-line" points="60,640 180,560 270,600 390,520 520,560 640,470 760,420 880,380 960,300"/>
    <circle class="chart-dot" cx="270" cy="600" r="6"/>
    <circle class="chart-dot" cx="640" cy="470" r="6"/>
    <circle class="chart-dot" cx="880" cy="380" r="6"/>
  </g>

  <path class="launch-beam" d="M502 692 C470 790 380 880 180 920 L180 989 L830 989 L830 920 C640 880 540 790 502 692 Z" fill="url(#beamFill)"/>

  <path class="host-photo host-photo--left" d="M0 600 L10 560 Q40 505 110 508 Q180 512 200 580 L205 690 Q270 700 300 760 L330 989 L0 989 Z" fill="url(#photoFill)" role="img" aria-label="Photo of the female course host in a denim jacket, smiling"/>
  <path class="host-photo host-photo--right" d="M717 989 L725 640 Q760 600 852 560 L855 520 Q870 476 905 476 Q950 478 960 520 L975 590 Q988 600 988 610 L988 989 Z" fill="url(#photoFill)" role="img" aria-label="Photo of the male course host in a black turtleneck, arms crossed"/>

  <g class="program-name">
    <text class="title-word" x="190" y="138" textLength="68" lengthAdjust="spacingAndGlyphs">THE</text>
    <rect class="title-box" x="268" y="72" width="404" height="70"/>
    <text class="title-word title-highlight" x="280" y="138" textLength="380" lengthAdjust="spacingAndGlyphs">LANTERN LEDGER</text>
    <text class="title-word" x="684" y="138" textLength="114" lengthAdjust="spacingAndGlyphs">PLAN</text>
  </g>

  <g class="headline">
    <text class="kicker" x="494" y="226" font-size="80" text-anchor="middle">HOW TO</text>
    <text class="headline-main" x="108" y="377" textLength="769" lengthAdjust="spacingAndGlyphs">LAUNCH</text>
    <text class="headline-sub" x="110" y="462" textLength="770" lengthAdjust="spacingAndGlyphs">A MULTI-MILLION BUSINESS</text>
    <text class="kicker" x="494" y="540" font-size="74" text-anchor="middle">FROM</text>
    <text class="headline-end" x="287" y="680" textLength="422" lengthAdjust="spacingAndGlyphs">SCR<tspan class="accent">A</tspan>TCH</text>
  </g>

  <g class="cta">
    <rect class="cta-box" x="371" y="871" width="247" height="60" rx="14"/>
    <text class="cta-label" x="494.5" y="909" text-anchor="middle">SIGN UP TODAY!</text>
  </g>
</svg>
</body>
</html>
```